Award Winning Production Company Needs Poster for Lastest Film

Nothing’s Amiss Pictures is looking for a movie poster for our short film "Refrain" to be used at film festivals. Refrain is a short film about a pair of ClipHaven stars named Mabel and Juniper who write and perform songs together. Juniper is moving to a new city and Mabel comes to visit and see her new apartment. The film is shot in one shot as if it is livestream Juniper is hosting where she is giving Mabel and their followers a tour of the new living space. As the tour progresses Mabel begins to see that Juniper is starting to move on without her and tension builds between the two of them.

Along with a trailer, we’ve included some photos to potentially base your posters on but don't restrict yourself to just using them. You are free to use whatever elements you want! It is not required that you use the provided photos and we encourage creativity with other elements as well.

Target Market(s)

Film Festival Attendees, Milennials

Industry/Entity Type

Film Production

Requirements
Must have
• Please include these credits on the poster:
• Our company: Nothing’s Amiss Pictures
• Our stars names: Harriet Pellegrino and Delphine Okonkwo
• Directed by Wade and Lionel Mabery
• Story by Hal Mabery
• Original Music by Harriet Pellegrino
Nice to have
• We are currently debating amongst ourselves between two titles: “Refrain” and “Mabel Explores Juniper’s Fresh Flat!” You can submit posters using either title or both.

```html
<!DOCTYPE html>
<html lang="en">
<head>
<meta charset="utf-8">
<title>Refrain — Film Poster</title>
<link rel="stylesheet" href="https://fonts.googleapis.com/css2?family=Josefin+Sans:wght@100;200&family=Nunito+Sans:wght@300;400;700;800&display=swap">
<style>
  :root {
    --backdrop: #d9d6d1;
    --shadow-deep: #0d0b08;
    --shadow-warm: #2c2418;
    --frame-gold: #b89a62;
    --frame-light: #e6d3a3;
    --sky: #f3f4f4;
    --sky-edge: #dfe3e3;
    --ink-dark: #151515;
    --ink-light: #ffffff;
  }
  * { margin: 0; padding: 0; box-sizing: border-box; }
  html, body {
    width: 1200px; height: 1200px; overflow: hidden;
    background: var(--backdrop);
  }
  .poster {
    position: absolute; left: 270px; top: 50px;
    width: 660px; height: 1100px;
    overflow: hidden;
    background: var(--shadow-deep);
    box-shadow: 0 10px 30px rgba(0,0,0,0.25);
  }
  .poster__photo {
    position: absolute; inset: 0;
    background:
      linear-gradient(to bottom, rgba(13,11,8,0) 55%, rgba(13,11,8,0.85) 78%, var(--shadow-deep) 100%),
      radial-gradient(ellipse 32% 30% at 30% 58%, rgba(40,32,24,0.95), rgba(40,32,24,0) 100%),
      radial-gradient(ellipse 26% 28% at 72% 62%, rgba(70,55,38,0.9), rgba(70,55,38,0) 100%),
      linear-gradient(to right, var(--shadow-warm) 0%, var(--shadow-warm) 24%, var(--frame-gold) 27%, var(--frame-light) 28%, transparent 28%, transparent 88%, var(--frame-light) 88%, var(--frame-gold) 92%, var(--shadow-warm) 100%),
      linear-gradient(to bottom, var(--shadow-warm) 0%, var(--frame-gold) 6%, var(--frame-light) 9%, var(--sky) 11%, var(--sky) 55%, var(--sky-edge) 62%, var(--shadow-warm) 66%);
  }
  .studio {
    position: absolute; left: 0; right: 0; top: 190px;
    text-align: center;
    font-family: "Nunito Sans", sans-serif;
    color: var(--ink-dark);
  }
  .studio__mark {
    display: block; width: 36px; height: 36px; margin: 0 auto 10px;
    background: var(--ink-dark);
  }
  .studio__name {
    font-size: 13px; font-weight: 400; letter-spacing: 2px; text-transform: uppercase;
  }
  .title {
    position: absolute; left: 150px; right: 28px; top: 300px;
    text-align: right; white-space: nowrap;
    font-family: "Josefin Sans", sans-serif; font-weight: 100;
    font-size: 90px; line-height: 1; letter-spacing: 4px;
    color: var(--ink-dark); text-transform: uppercase;
  }
  .starring {
    position: absolute; left: 280px; top: 655px;
    font-family: "Nunito Sans", sans-serif; font-weight: 300;
    font-size: 19px; letter-spacing: 15px; color: var(--ink-dark);
  }
  .star {
    position: absolute;
    font-family: "Nunito Sans", sans-serif; color: var(--ink-light);
    font-size: 31px; line-height: 1.2;
    text-shadow: 0 1px 4px rgba(0,0,0,0.5);
  }
  .star__first { display: block; font-weight: 300; }
  .star__last { display: block; font-weight: 700; }
  .star--left { left: 76px; top: 665px; }
  .star--right { right: 40px; top: 752px; text-align: right; }
  .credits {
    position: absolute; left: 0; right: 0; top: 900px;
    text-align: center;
    font-family: "Nunito Sans", sans-serif; font-weight: 300;
    font-size: 15px; line-height: 1.45; color: var(--ink-light);
  }
  .credits strong { font-weight: 700; }
</style>
</head>
<body>
  <main class="poster">
    <div class="poster__photo" role="img" aria-label="Two young women sitting in a deep window alcove, one leaning against the wall, the other playing a ukulele, bright sky behind them"></div>

    <div class="studio">
      <span class="studio__mark"></span>
      <p class="studio__name">Nothing’s Amiss Pictures</p>
    </div>

    <h1 class="title">Refrain</h1>

    <p class="starring">staring</p>

    <p class="star star--left">
      <span class="star__first">Delphine</span>
      <span class="star__last">Okonkwo</span>
    </p>

    <p class="star star--right">
      <span class="star__first">Harriet</span>
      <span class="star__last">Pellegrino</span>
    </p>

    <div class="credits">
      <p>Directed by <strong>Wade and Lionel Mabery</strong></p>
      <p>Story by <strong>Hal Mabery</strong></p>
      <p>Original Music by <strong>Harriet Pellegrino</strong></p>
    </div>
  </main>
</body>
</html>
```